Www.zubwave.com monthly sweepstakes.

Every month I am giving away 1st place $500 gift card to your local RC hobby shop of choice, 2nd place $100 gift card 3rd place ZubWave merch. All things rc: cars, boats, quadcopters, helicopters, airplanes.

Needs to be with the color theme of the website. Check zubwave.com for current sweepstakes banner. New banner should be half the size in height. I will post dimension later.

Target Market(s)

Rc hobbies cars airplanes helicopters boats

Industry/Entity Type

RemoteControl hobbies

Requirements
Must have
• 1440x680 size, Blend with black background, creative and in incorporate all trypes of rc craft
Should not have
• To many different colors, dosnt need logo as its already on website. This is a banner for my homepage

```html
<!DOCTYPE html>
<html lang="en">
<head>
<meta charset="UTF-8">
<title>ZubWave Monthly Sweepstakes Banner</title>
<link href="https://fonts.googleapis.com/css2?family=Poppins:wght@400;600;700&family=Russo+One&display=swap" rel="stylesheet">
<style>
  :root {
    --bg: #111111;
    --ink: #ffffff;
    --crimson: #a3111c;
    --gold-1: #f3d39a;
    --gold-2: #c99a5a;
    --gold-3: #e8bf82;
    --rule: #4a4a4a;
  }
  html, body {
    margin: 0;
    padding: 0;
    width: 1200px;
    height: 567px;
    overflow: hidden;
    background: var(--bg);
  }
  .banner {
    position: relative;
    width: 1200px;
    height: 567px;
    overflow: hidden;
    background: var(--bg);
  }
  .banner__inner {
    position: absolute;
    left: 0;
    top: 0;
    width: 1440px;
    height: 680px;
    transform: scale(0.833333);
    transform-origin: 0 0;
    font-family: "Poppins", sans-serif;
    color: var(--ink);
  }
  .craft-panels {
    position: absolute;
    inset: 0;
    width: 1440px;
    height: 680px;
  }
  .headline {
    position: absolute;
    left: 445px;
    top: 58px;
    width: 630px;
    text-align: center;
    font-family: "Russo One", sans-serif;
    background: linear-gradient(180deg, var(--gold-1) 0%, var(--gold-3) 45%, var(--gold-2) 100%);
    -webkit-background-clip: text;
    background-clip: text;
    color: transparent;
    margin: 0;
    font-weight: 400;
  }
  .headline__win {
    display: block;
    font-size: 132px;
    line-height: 1;
    letter-spacing: 4px;
  }
  .headline__sub {
    display: block;
    margin-top: 16px;
    font-size: 40px;
    line-height: 1;
    letter-spacing: 1px;
  }
  .prize {
    position: absolute;
    display: flex;
    align-items: flex-start;
  }
  .prize__medal {
    width: 50px;
    height: 50px;
    flex: none;
  }
  .prize__place {
    font-size: 24px;
    font-weight: 400;
    margin: 11px 24px 0 8px;
    letter-spacing: 0.5px;
  }
  .prize__amount {
    font-size: 52px;
    font-weight: 700;
    color: var(--crimson);
    line-height: 1;
    margin-right: 8px;
  }
  .prize__detail {
    font-size: 26px;
    line-height: 1.25;
    margin-top: 16px;
  }
  .prize--first { left: 267px; top: 358px; }
  .prize--second { left: 263px; top: 493px; }
  .prize--third { left: 267px; top: 605px; }
  .prize--first .prize__text { margin-top: -8px; }
  .prize--first .prize__detail--wrap { margin-top: 0; display: block; }
  .prize__merch {
    font-size: 40px;
    font-weight: 700;
    color: var(--crimson);
    line-height: 1;
    margin-top: 3px;
  }
  .divider {
    position: absolute;
    height: 0;
    border-top: 2px dashed var(--rule);
  }
  .divider--one { left: 195px; top: 456px; width: 663px; }
  .divider--two { left: 175px; top: 584px; width: 670px; }
</style>
</head>
<body>
<div class="banner">
  <div class="banner__inner">
    <svg class="craft-panels" viewBox="0 0 1440 680" xmlns="http://www.w3.org/2000/svg">
      <defs>
        <linearGradient id="boatTone" x1="0" y1="0" x2="1" y2="1">
          <stop offset="0" stop-color="#8a7d66"/>
          <stop offset="0.5" stop-color="#d9782a"/>
          <stop offset="1" stop-color="#6b5a44"/>
        </linearGradient>
        <linearGradient id="droneTone" x1="0" y1="0" x2="1" y2="1">
          <stop offset="0" stop-color="#e9e6e1"/>
          <stop offset="0.45" stop-color="#6fb9c4"/>
          <stop offset="0.7" stop-color="#d93a4a"/>
          <stop offset="1" stop-color="#dcd8d2"/>
        </linearGradient>
        <linearGradient id="carTone" x1="0" y1="0" x2="0" y2="1">
          <stop offset="0" stop-color="#8fb4cf"/>
          <stop offset="0.25" stop-color="#8e8a6e"/>
          <stop offset="0.5" stop-color="#e08a2a"/>
          <stop offset="0.8" stop-color="#8a7a62"/>
          <stop offset="1" stop-color="#c7b9a0"/>
        </linearGradient>
        <linearGradient id="heliTone" x1="0" y1="0" x2="0" y2="1">
          <stop offset="0" stop-color="#b9bcc0"/>
          <stop offset="0.35" stop-color="#55564a"/>
          <stop offset="0.65" stop-color="#4a4b3f"/>
          <stop offset="1" stop-color="#7b7566"/>
        </linearGradient>
        <linearGradient id="jetTone" x1="0" y1="0" x2="1" y2="1">
          <stop offset="0" stop-color="#9dc3e6"/>
          <stop offset="0.55" stop-color="#cf3a45"/>
          <stop offset="1" stop-color="#6fa6d8"/>
        </linearGradient>
      </defs>
      <polygon points="0,0 190,0 118,150 0,150" fill="url(#boatTone)" role="img" aria-label="Photo of an orange RC boat on a workbench"/>
      <polygon points="208,0 545,0 312,292 132,152" fill="url(#droneTone)" role="img" aria-label="Photo of a racing quadcopter with red propellers on a scale"/>
      <polygon points="0,250 96,140 298,292 22,680 0,680" fill="url(#carTone)" role="img" aria-label="Photo of an orange RC off-road truck climbing a rocky hill"/>
      <polygon points="1310,0 1440,0 1440,322 1152,680 770,680" fill="url(#heliTone)" role="img" aria-label="Photo of an olive scale RC attack helicopter with shark-teeth nose art in flight"/>
      <polygon points="1440,344 1440,680 1170,680" fill="url(#jetTone)" role="img" aria-label="Photo of a red and white RC jet flying against a blue sky"/>
    </svg>

    <h1 class="headline">
      <span class="headline__win">WIN</span>
      <span class="headline__sub">AN RC SHOPPING SPREE!</span>
    </h1>

    <div class="prize prize--first">
      <svg class="prize__medal" viewBox="0 0 50 50" aria-hidden="true">
        <circle cx="25" cy="25" r="24" fill="#c9a24a"/>
        <circle cx="25" cy="25" r="18" fill="#8e1018"/>
        <text x="25" y="32" text-anchor="middle" font-family="Poppins, sans-serif" font-weight="700" font-size="20" fill="#f0d79a">1</text>
      </svg>
      <span class="prize__place">PLACE</span>
      <div class="prize__text">
        <span class="prize__amount">$500</span><span class="prize__detail">gift card to your</span>
        <span class="prize__detail prize__detail--wrap">local hobby shop.</span>
      </div>
    </div>

    <div class="divider divider--one"></div>

    <div class="prize prize--second">
      <svg class="prize__medal" viewBox="0 0 50 50" aria-hidden="true">
        <circle cx="25" cy="25" r="24" fill="#d9d9d9"/>
        <circle cx="25" cy="25" r="18" fill="#ededed" stroke="#a8a8a8" stroke-width="2"/>
        <text x="25" y="32" text-anchor="middle" font-family="Poppins, sans-serif" font-weight="700" font-size="20" fill="#8a8a8a">2</text>
      </svg>
      <span class="prize__place">PLACE</span>
      <span class="prize__amount">$100</span><span class="prize__detail">gift card.</span>
    </div>

    <div class="divider divider--two"></div>

    <div class="prize prize--third">
      <svg class="prize__medal" viewBox="0 0 50 50" aria-hidden="true">
        <circle cx="25" cy="25" r="24" fill="#e08a43"/>
        <circle cx="25" cy="25" r="18" fill="#f0a25c"/>
        <text x="25" y="32" text-anchor="middle" font-family="Poppins, sans-serif" font-weight="700" font-size="20" fill="#b35f1f">3</text>
      </svg>
      <span class="prize__place">PLACE</span>
      <span class="prize__merch">ZubWave Merch</span>
    </div>
  </div>
</div>
</body>
</html>
```